This book will apply the 12 Steps to gaming addiction, also known as video game addiction. The primary purpose of the book is to provide an effective solution for this new type of addiction. The solution is based on the rich and successful concepts of traditional twelve-step programs like RL.

The title on the cover will be "Nine Doors Past the Glowing Screen" and "by Martin Quorby". A subtitle can be used if it works in your design of "A Practical Path Beyond Compulsive Console Play". Cover will be for a 6" x 9" book approximately 110 pages in length.

Some back cover text including some review quotes and an author bio are in the attached Word doc. There is also an author photo attached for for the back cover.

Requirements
Must have
• For the cover design it could be stylized, or an image, a partial image, or whatever. I am open to suggestions. Think about what would be noticed by a person searching for help with moderating their video game use, or by the parents or loved ones of problem gamers. Something contemporary and eye catching.

```html
<!DOCTYPE html>
<html lang="en">
<head>
<meta charset="utf-8">
<title>Nine Doors Past the Glowing Screen — Cover</title>
<link href="https://fonts.googleapis.com/css2?family=Playfair+Display:wght@400;700;900&display=swap" rel="stylesheet">
<style>
  :root {
    --backdrop: #e6e6e6;
    --teal: #3e9584;
    --teal-dark: #2f7668;
    --spine-shade: #2c6e61;
    --ink-light: #f1f1ee;
    --glow: #5fb3a2;
    --pale: #e4e4e2;
  }
  * { margin: 0; padding: 0; box-sizing: border-box; }
  html, body {
    width: 1200px;
    height: 800px;
    overflow: hidden;
    background: var(--backdrop);
  }
  .canvas {
    position: relative;
    width: 1200px;
    height: 800px;
  }
  .book-cover {
    position: absolute;
    left: 350px;
    top: 20px;
    width: 500px;
    height: 760px;
    background: var(--teal);
    overflow: hidden;
    border-radius: 2px 4px 4px 2px;
  }
  .cover-bands {
    position: absolute;
    inset: 0;
    width: 100%;
    height: 100%;
  }
  .spine-edge {
    position: absolute;
    left: 0;
    top: 0;
    width: 22px;
    height: 100%;
    background: linear-gradient(to right, var(--spine-shade) 0 16px, rgba(255,255,255,0.08) 16px 18px, transparent 18px);
  }
  .title-block {
    position: absolute;
    left: 22px;
    right: 0;
    top: 26px;
    text-align: center;
    color: var(--ink-light);
    font-family: "Playfair Display", Georgia, serif;
    line-height: 1;
  }
  .title-line-top {
    display: block;
    font-weight: 700;
    white-space: nowrap;
  }
  .title-small {
    font-size: 30px;
    letter-spacing: 1px;
  }
  .title-large {
    font-size: 56px;
    letter-spacing: 1px;
    margin: 0 8px;
  }
  .title-line-middle {
    display: block;
    font-weight: 400;
    font-size: 50px;
    margin-top: 6px;
  }
  .title-line-bottom {
    display: block;
    font-weight: 900;
    font-size: 76px;
    letter-spacing: 1px;
    margin-top: 4px;
  }
  .cover-illustration {
    position: absolute;
    left: 66px;
    top: 215px;
    width: 370px;
    height: 478px;
    border-radius: 50% 50% 24% 34% / 40% 40% 22% 26%;
    background: radial-gradient(ellipse 46% 22% at 58% 38%, var(--pale) 0%, var(--pale) 55%, rgba(228,228,226,0) 100%),
                radial-gradient(ellipse at 52% 42%, var(--glow) 0%, rgba(95,179,162,0.75) 45%, rgba(62,149,132,0) 78%);
  }
  .author-name {
    position: absolute;
    left: 22px;
    right: 0;
    top: 702px;
    text-align: center;
    color: var(--ink-light);
    font-family: "Playfair Display", Georgia, serif;
    font-size: 17px;
    letter-spacing: 9px;
    text-transform: uppercase;
  }
</style>
</head>
<body>
  <div class="canvas">
    <div class="book-cover">
      <svg class="cover-bands" viewBox="0 0 500 760" preserveAspectRatio="none" aria-hidden="true">
        <polygon points="160,0 234,0 0,268 0,183" fill="var(--teal-dark)" opacity="0.55"/>
        <polygon points="450,0 500,0 500,35 0,590 0,520" fill="var(--teal-dark)" opacity="0.55"/>
        <polygon points="500,210 500,320 0,890 0,780" fill="var(--teal-dark)" opacity="0.55"/>
        <polygon points="500,440 500,520 260,760 175,760" fill="var(--teal-dark)" opacity="0.55"/>
      </svg>
      <div class="spine-edge"></div>

      <h1 class="title-block">
        <span class="title-line-top"><span class="title-small">NINE</span><span class="title-large">DOORS</span><span class="title-small">PAST</span></span>
        <span class="title-line-middle">THE GLOWING</span>
        <span class="title-line-bottom">SCREEN</span>
      </h1>

      <div class="cover-illustration" role="img" aria-label="Line drawing of a head in profile with a light grey game controller inside it, its white cable trailing down and looping out of the head"></div>

      <p class="author-name">Martin Quorby</p>
    </div>
  </div>
</body>
</html>
```